Recycling and Rubbish services for Residential and Commercial customers

We are after a complete redesign or freshening up of our current website.
www.tidlowe.co.nz
On this site the general public can rent or buy rollaTUBs or skips for rubbish and recycling collection around the Nelson and Tasman area of New Zealand.

Target Market(s)

18 to 100 year old males and females in Nelson and Tasman area of New Zealand

Industry/Entity Type

Waste Management

Contact Information for Business Card

logo name title email phone web site address all the normal stuff

Number of Pages Required

5+ page

Colors

Designer to choose colors to be used in the design.

Requirements
Must have
• Has to be very fast and easy for the customer to rent bin, skip, tags, liner etc..
• see web site www.tidlowe.co.nz
• An address finder so we can show two rates for urban and rural streets
Nice to have
• "We’re trying to get back to a more human face. Our customers appreciate that we are locals too. We are proud to be able to support our local community through sponsorship and donations."

```html
<!DOCTYPE html>
<html lang="en">
<head>
<meta charset="utf-8">
<title>Tidlowe — Recycling &amp; Rubbish Services</title>
<link href="https://fonts.googleapis.com/css2?family=Open+Sans:wght@400;600;700;800&display=swap" rel="stylesheet">
<style>
:root{
  --red:#e3222b;
  --red-dark:#b8141c;
  --black:#111111;
  --panel:#3a3a3a;
  --grey:#f1f1f1;
  --line:#dddddd;
  --text:#222222;
  --muted:#666666;
  --white:#ffffff;
  --bin-green:#2f6b33;
}
*{box-sizing:border-box;margin:0;padding:0}
html,body{width:1200px;height:4204px;overflow:hidden}
body{font-family:"Open Sans",Arial,sans-serif;color:var(--text);background:var(--white)}
a{color:inherit;text-decoration:none}
.btn{display:inline-flex;align-items:center;gap:10px;background:var(--red);color:var(--white);font-weight:700;text-transform:uppercase;font-size:15px;padding:14px 26px;border-radius:3px}
.btn-sm{font-size:11px;padding:10px 16px}
.section-title{text-align:center;font-weight:800;font-size:34px;text-transform:uppercase;letter-spacing:.5px}
.section-title::after{content:"";display:block;width:60px;height:3px;background:var(--red);margin:12px auto 0}
.ph{border-radius:4px}

/* header */
.site-header{height:120px;display:flex;align-items:center;justify-content:space-between;padding:0 60px}
.brand{background:var(--red);color:var(--white);font-weight:800;font-size:30px;line-height:1;padding:14px 18px;width:150px;height:92px;display:flex;align-items:flex-end}
.search{width:480px;height:44px;border:1px solid var(--line);border-radius:3px;display:flex;align-items:center;justify-content:space-between;padding:0 16px;color:#999;font-size:15px}
.contact-top{text-align:right}
.contact-top .phone{color:var(--red);font-weight:700;font-size:22px;display:flex;align-items:center;gap:8px;justify-content:flex-end}
.contact-top .cart{font-size:13px;color:var(--muted);margin-top:4px}

/* nav */
.main-nav{height:60px;background:var(--black);display:flex;align-items:center;padding:0 60px;gap:6px}
.main-nav a{color:var(--white);font-weight:700;font-size:15px;text-transform:uppercase;padding:0 20px;height:60px;display:flex;align-items:center}
.main-nav a.active{border-bottom:4px solid var(--red)}

/* hero */
.hero{height:480px;position:relative;background:linear-gradient(180deg,#6e6a66 0%,#8d8780 45%,#4a4643 100%);overflow:hidden}
.hero-bins{position:absolute;right:60px;top:80px;width:500px;height:360px;background:linear-gradient(90deg,#c72a25 0%,#d9c23a 30%,#2c63b5 55%,#c94a22 75%,#6b6b6b 100%);opacity:.85}
.hero-copy{position:absolute;left:60px;top:170px;color:var(--white)}
.hero-copy .kicker{font-size:34px;font-weight:400;text-transform:uppercase}
.hero-copy h1{font-size:36px;font-weight:800;text-transform:uppercase;line-height:1.2;max-width:620px;margin-top:4px}
.hero-copy .btn{margin-top:30px}

/* address */
.address-bar{height:180px;background:var(--black);display:flex;flex-direction:column;align-items:center;justify-content:center;gap:26px}
.address-bar p{color:var(--white);font-size:17px}
.address-bar p strong{color:var(--red);font-weight:600}
.address-input{width:760px;height:52px;background:var(--white);border-radius:3px;display:flex;align-items:center;justify-content:space-between;padding:0 20px;font-size:15px;color:#777}

/* products */
.products{height:980px;background:var(--grey);padding-top:60px}
.product-grid{display:grid;grid-template-columns:520px 520px;gap:70px 40px;justify-content:center;margin-top:60px}
.product-card{background:var(--white);height:370px;box-shadow:0 2px 6px rgba(0,0,0,.12);padding:60px 30px 0;position:relative}
.product-card h3{font-size:26px;font-weight:800;text-transform:uppercase}
.product-card p{font-size:14px;color:var(--muted);width:240px;margin:8px 0 26px;line-height:1.4}
.product-card .ph{position:absolute;right:40px;bottom:50px;width:170px;height:200px;background:linear-gradient(180deg,#3f8a45,var(--bin-green))}
.product-card.wide .ph{width:230px;height:130px}

/* pay */
.pay{height:360px;background:linear-gradient(135deg,var(--red) 0%,#c4161e 100%);color:var(--white);display:flex;flex-direction:column;align-items:center;padding-top:60px}
.pay .section-title::after{background:var(--white)}
.pay .sub{font-size:18px;margin-top:14px}
.select{width:900px;height:50px;background:var(--white);border-radius:3px;display:flex;align-items:center;justify-content:space-between;padding:0 18px;color:#444;font-size:14px;margin-top:24px}
.btn-dark{background:var(--black);margin-top:30px}

/* change bin */
.change-bin{height:580px;display:flex;padding:40px 60px 0;gap:50px}
.change-copy{width:490px}
.change-copy h2{font-size:38px;font-weight:800;text-transform:uppercase}
.change-copy h4{font-size:20px;font-weight:800;margin:18px 0 10px}
.change-copy p{font-size:15px;line-height:1.45}
.bins-row{display:flex;gap:24px;margin-top:30px}
.bins-row .ph{width:140px;height:220px;background:linear-gradient(180deg,#3f8a45,var(--bin-green))}
.bin-panel{flex:1;background:var(--panel);height:500px;padding:40px 50px}
.bin-panel h3{color:var(--white);font-size:36px;font-weight:700;text-align:center;margin-bottom:30px}
.bin-panel .select{width:100%;height:44px;margin-top:22px;font-style:italic}
.bin-panel .btn{margin:34px auto 0;display:flex;width:max-content}

/* collection */
.collection{height:560px;background:var(--grey);padding-top:50px;text-align:center}
.collection .addr{font-weight:700;font-size:20px;margin-top:24px}
.map{width:1080px;height:300px;margin:26px auto 0;background:linear-gradient(180deg,#aad3df 0%,#cfe6d0 50%,#e8e4d8 100%);position:relative}
.map-tabs{position:absolute;left:10px;top:10px;background:var(--white);display:flex;font-size:13px;box-shadow:0 1px 3px rgba(0,0,0,.3)}
.map-tabs span{padding:6px 12px}
.collection .note{font-size:15px;margin-top:22px}

/* change address */
.change-address{height:300px;position:relative;background:var(--white);display:flex;flex-direction:column;align-items:center;padding-top:56px;overflow:hidden}
.change-address .corner{position:absolute;width:0;height:0}
.corner.tl{left:0;top:0;border-top:110px solid var(--red);border-right:220px solid transparent}
.corner.br{right:0;bottom:0;border-bottom:110px solid var(--red);border-left:220px solid transparent}
.change-address .link{color:var(--red);font-style:italic;text-decoration:underline;font-size:16px;margin:24px 0 26px}

/* quick buy */
.quick-buy{height:280px;padding-top:30px;text-align:center}
.carousel{display:flex;align-items:center;justify-content:space-between;padding:0 30px;margin-top:36px}
.carousel .items{display:flex;gap:110px;align-items:center}
.carousel .ph{width:90px;height:120px;background:linear-gradient(180deg,#4a7c4e,#2f5a33)}
.carousel .ph.tag{background:linear-gradient(180deg,#3aa8e0,#1e7fb5);width:50px}
.carousel .ph.label{background:linear-gradient(180deg,#e84045,#c21a20);width:70px}

/* footer */
.site-footer{height:304px;background:var(--black);color:var(--white);display:flex;padding:40px 60px 0;gap:110px}
.footer-brand .tagline{font-size:13px;font-weight:700;margin-bottom:10px}
.footer-brand .brand{width:200px;height:130px;font-size:40px}
.footer-brand .copy{font-size:13px;color:#bbb;margin-top:14px}
.site-footer h5{color:var(--red);font-size:20px;font-weight:700;text-transform:uppercase;margin-bottom:10px}
.links a{display:block;font-size:15px;line-height:1.55}
.touch li{list-style:none;display:flex;align-items:center;gap:14px;font-size:15px;margin-bottom:18px}
.social{display:flex;gap:14px;margin-top:8px}
.social span{width:30px;height:30px;border-radius:50%;background:#444}
</style>
</head>
<body>

<header class="site-header">
  <a class="brand" href="#">TIDLOWE</a>
  <div class="search">Search here
    <svg width="18" height="18" viewBox="0 0 18 18"><circle cx="7.5" cy="7.5" r="5.5" fill="none" stroke="#333" stroke-width="2"/><line x1="11.5" y1="11.5" x2="16" y2="16" stroke="#333" stroke-width="2"/></svg>
  </div>
  <div class="contact-top">
    <div class="phone"><svg width="18" height="18" viewBox="0 0 24 24"><path fill="#e3222b" d="M6.6 10.8a15 15 0 0 0 6.6 6.6l2.2-2.2c.3-.3.7-.4 1-.2 1.1.4 2.3.6 3.6.6.6 0 1 .4 1 1V20c0 .6-.4 1-1 1C10.6 21 3 13.4 3 4c0-.6.4-1 1-1h3.5c.6 0 1 .4 1 1 0 1.3.2 2.5.6 3.6.1.3 0 .7-.2 1z"/></svg>(03) 555 0190</div>
    <div class="cart">Cart · 0 items</div>
  </div>
</header>

<nav class="main-nav">
  <a class="active" href="#">Home</a><a href="#">About Us</a><a href="#">Products</a><a href="#">Buy Bin</a><a href="#">Rent Bin</a><a href="#">Contact Us</a>
</nav>

<section class="hero">
  <div class="hero-bins ph" role="img" aria-label="Row of coloured rubbish bins in red, yellow, blue, orange and grey"></div>
  <div class="hero-copy">
    <div class="kicker">Recycling &amp; Rubbish Services</div>
    <h1>For Residental &amp; Comercial Customers</h1>
    <a class="btn" href="#">Buy Now <svg width="16" height="16" viewBox="0 0 16 16"><circle cx="8" cy="8" r="8" fill="#fff"/><path d="M6 4l4 4-4 4" stroke="#e3222b" stroke-width="2" fill="none"/></svg></a>
  </div>
</section>

<section class="address-bar">
  <p><strong>9 UNSPECIFIED URBAN ADDRESS, NO TOWN</strong> is where your service will be collected from.</p>
  <div class="address-input">Change your location...
    <svg width="14" height="14" viewBox="0 0 14 14"><path d="M2 4l5 5 5-5" stroke="#e3222b" stroke-width="2" fill="none"/></svg>
  </div>
</section>

<section class="products">
  <h2 class="section-title">Products Range</h2>
  <div class="product-grid">
    <article class="product-card">
      <h3>Tidlowe Bin</h3>
      <p>Cum sociis natoque penatibus et magnis dis</p>
      <a class="btn btn-sm" href="#">Get your bin here</a>
      <div class="ph" role="img" aria-label="Green rubbish bin with blue lid"></div>
    </article>
    <article class="product-card wide">
      <h3>Tidlowe Skip</h3>
      <p>Cum sociis natoque penatibus et magnis dis parturient montes, nascetur</p>
      <a class="btn btn-sm" href="#">Get your skip here</a>
      <div class="ph" role="img" aria-label="Green steel skip"></div>
    </article>
    <article class="product-card wide">
      <h3>Commercial Bin</h3>
      <p>Lorem ipsum dolor sit amet, consectetuer adipiscing elit. Aenean commodo</p>
      <a class="btn btn-sm" href="#">Get commercial bins</a>
      <div class="ph" role="img" aria-label="Large green commercial waste container"></div>
    </article>
    <article class="product-card">
      <h3>Bin Supplies</h3>
      <p>Lorem ipsum dolor sit amet, consectetuer adipiscing elit.</p>
      <a class="btn btn-sm" href="#">Get bin supplies</a>
      <div class="ph" role="img" aria-label="Green rubbish bin with blue lid"></div>
    </article>
  </div>
</section>

<section class="pay">
  <h2 class="section-title">Pay My Account</h2>
  <div class="sub">Please Select Your Payment Type</div>
  <div class="select">Pay By Credit Card or Account By Account
    <svg width="12" height="12" viewBox="0 0 12 12"><path d="M1 3l5 5 5-5" fill="#333"/></svg>
  </div>
  <a class="btn btn-dark" href="#">Fill Our Form <svg width="16" height="16" viewBox="0 0 16 16"><circle cx="8" cy="8" r="8" fill="#fff"/><path d="M6 4l4 4-4 4" stroke="#111" stroke-width="2" fill="none"/></svg></a>
</section>

<section class="change-bin">
  <div class="change-copy">
    <h2>Change Bin Size</h2>
    <h4>RENTAL - Red Service customers only</h4>
    <p>In order to change your bin size your rental must be due for payment now.<br>The change of bin will occur on your next collection day.<br>A $8.00 Bin change fee will be charged</p>
    <div class="bins-row">
      <div class="ph" role="img" aria-label="Green bin with yellow lid"></div>
      <div class="ph" role="img" aria-label="Green bin with green lid"></div>
      <div class="ph" role="img" aria-label="Green bin with red lid"></div>
    </div>
  </div>
  <div class="bin-panel">
    <h3>Select Your Bin Size</h3>
    <div class="select">Your Current Bin Size <svg width="10" height="10" viewBox="0 0 12 12"><path d="M1 3l5 5 5-5" fill="#333"/></svg></div>
    <div class="select">Your New Bin Size <svg width="10" height="10" viewBox="0 0 12 12"><path d="M1 3l5 5 5-5" fill="#333"/></svg></div>
    <div class="select">Payment Interval <svg width="10" height="10" viewBox="0 0 12 12"><path d="M1 3l5 5 5-5" fill="#333"/></svg></div>
    <div class="select">Customer ID <svg width="10" height="10" viewBox="0 0 12 12"><path d="M1 3l5 5 5-5" fill="#333"/></svg></div>
    <a class="btn btn-sm" href="#">Add your contact detail</a>
  </div>
</section>

<section class="collection">
  <h2 class="section-title">Your Collection Day</h2>
  <div class="addr">Collection address: 9 UNSPECIFIED URBAN ADDRESS, NO TOWN</div>
  <div class="map" role="img" aria-label="World map with a route line ending at a pin on Nelson, New Zealand">
    <div class="map-tabs"><span>Map</span><span>Satellite</span></div>
  </div>
  <p class="note">Please contact the office on 555 0190 to have your address verified.</p>
</section>

<section class="change-address">
  <span class="corner tl"></span><span class="corner br"></span>
  <h2 class="section-title">Change My Address</h2>
  <a class="link" href="#">Please click here to check your new collection day and if we service your new address.</a>
  <a class="btn" href="#">Change My Address</a>
</section>

<section class="quick-buy">
  <h2 class="section-title">Quick Buy Supplies</h2>
  <div class="carousel">
    <svg width="16" height="24" viewBox="0 0 16 24"><path d="M12 2L3 12l9 10" stroke="#111" stroke-width="3" fill="none"/></svg>
    <div class="items">
      <div class="ph" role="img" aria-label="Roll of bin liners"></div>
      <div class="ph" role="img" aria-label="Pack of 120L bin liners"></div>
      <div class="ph" role="img" aria-label="Pack of 240L bin liners"></div>
      <div class="ph tag" role="img" aria-label="Blue collection tag"></div>
      <div class="ph label" role="img" aria-label="Red rubbish bag tag"></div>
    </div>
    <svg width="16" height="24" viewBox="0 0 16 24"><path d="M4 2l9 10-9 10" stroke="#111" stroke-width="3" fill="none"/></svg>
  </div>
</section>

<footer class="site-footer">
  <div class="footer-brand">
    <div class="tagline">Putting WASTE in its Place!</div>
    <a class="brand" href="#">TIDLOWE</a>
    <div class="copy">© 2017 Tidlowe · 14 Orchard Rd</div>
  </div>
  <div class="links">
    <h5>Special Links</h5>
    <a href="#">Home</a><a href="#">About Us</a><a href="#">FAQ</a><a href="#">Media</a><a href="#">Links</a>
  </div>
  <div class="touch">
    <h5>Get in Touch With Us</h5>
    <ul>
      <li><svg width="16" height="20" viewBox="0 0 16 20"><path fill="#fff" d="M8 0a7 7 0 0 0-7 7c0 5 7 13 7 13s7-8 7-13a7 7 0 0 0-7-7zm0 10a3 3 0 1 1 0-6 3 3 0 0 1 0 6z"/></svg>12 Harbour Lane, Nelson, 7010, New Zealand</li>
      <li><svg width="18" height="14" viewBox="0 0 18 14"><rect width="18" height="14" fill="#fff"/><path d="M0 0l9 7 9-7" stroke="#111" stroke-width="1.5" fill="none"/></svg>info@tidlowe.co.nz</li>
      <li><svg width="16" height="16" viewBox="0 0 24 24"><path fill="#fff" d="M6.6 10.8a15 15 0 0 0 6.6 6.6l2.2-2.2c.3-.3.7-.4 1-.2 1.1.4 2.3.6 3.6.6.6 0 1 .4 1 1V20c0 .6-.4 1-1 1C10.6 21 3 13.4 3 4c0-.6.4-1 1-1h3.5c.6 0 1 .4 1 1 0 1.3.2 2.5.6 3.6.1.3 0 .7-.2 1z"/></svg>(03) 555 0190</li>
    </ul>
    <div class="social"><span></span><span></span><span></span><span></span><span></span></div>
  </div>
</footer>

</body>
</html>
```